We are looking for a poster / flyer to advertise our Squash Tournament - the Wrenfold Club Sydney CBD Squash Open. I have provided the details and sponsor logos that need to appear on the poster in the attachments.
I am open to the poster including pictures of real life squash playing action shots or a complete graphic art design.

Target Market(s)

Squash Players and Sporty People who may be interested in trying Squash as a new Sport

Requirements
Must have
• 1. All logos attached in files (logos in the word doc and the Bramwick Logo)
2. Content that has been provided in the word doc
3. Printable on A3 paper
4. Title of the poster must be 2021 Wrenfold Club Sydney CBD Squash Open
Nice to have
• 1.Design must be related to the Sport of Squash (can either be a graphic Design that incorporates a real life squash pic rom the internet or 100% graphic)
2. Something incorporating both female and junior squash player participation.
3. Poster depicts action / athleticism.

```html
<!DOCTYPE html>
<html lang="en">
<head>
<meta charset="utf-8">
<title>2021 Wrenfold Club Sydney CBD Squash Open</title>
<link rel="stylesheet" href="https://fonts.googleapis.com/css2?family=Alfa+Slab+One&family=Montserrat:ital,wght@0,400;0,600;0,700;0,800;1,500&family=Oswald:wght@500;700&display=swap">
<style>
  :root {
    --orange: #f6a925;
    --orange-light: #ffc65a;
    --navy: #1c2b4b;
    --ink: #101828;
    --white: #ffffff;
    --photo-dark: #141a22;
    --photo-mid: #3b4654;
  }
  * { box-sizing: border-box; margin: 0; padding: 0; }
  html, body { width: 849px; height: 1200px; overflow: hidden; background: var(--orange); }
  .poster {
    position: relative; width: 849px; height: 1200px; overflow: hidden;
    background: var(--orange); font-family: "Montserrat", sans-serif; color: var(--navy);
  }
  .brand-mark {
    position: absolute; left: 22px; top: 16px; width: 106px; height: 36px;
    background: var(--white); display: flex; align-items: center; justify-content: center;
    font-family: "Montserrat", sans-serif; font-weight: 800; font-size: 17px; letter-spacing: 1px; color: var(--ink);
  }
  .title-club {
    position: absolute; left: 0; right: 0; top: 56px; text-align: center;
    font-family: "Alfa Slab One", serif; font-size: 76px; line-height: 1; color: var(--navy); letter-spacing: 1px;
  }
  .title-band {
    position: absolute; left: 132px; top: 142px; width: 410px; height: 38px; background: var(--navy);
    color: var(--white); font-family: "Alfa Slab One", serif; font-size: 25px; line-height: 38px; text-align: center;
  }
  .title-year {
    position: absolute; left: 552px; top: 130px; font-family: "Alfa Slab One", serif; font-size: 56px; line-height: 1; color: var(--navy);
  }
  .action-photo {
    position: absolute; left: 0; top: 204px; width: 849px; height: 626px;
    background: radial-gradient(ellipse at 72% 45%, var(--photo-mid) 0%, var(--photo-dark) 70%);
  }
  .prize {
    position: absolute; left: 110px; top: 246px; background: var(--white); color: var(--navy);
    padding: 4px 14px; font-family: "Montserrat", sans-serif; font-weight: 800; font-size: 30px;
  }
  .entries-close {
    position: absolute; left: 112px; top: 296px; color: var(--white);
    font-weight: 700; font-size: 27px; line-height: 1.2;
  }
  .grades-heading {
    position: absolute; left: 88px; top: 622px; color: var(--white);
    font-family: "Oswald", sans-serif; font-weight: 500; font-size: 38px; letter-spacing: 1px;
  }
  .grades-list {
    position: absolute; left: 90px; top: 672px; width: 440px; list-style: none;
    display: grid; grid-template-columns: 200px 240px; row-gap: 2px;
    color: var(--orange-light); font-weight: 600; font-size: 17px; line-height: 1.3;
  }
  .grades-list li::before { content: "• "; }
  .grades-note { position: absolute; left: 110px; top: 752px; color: var(--white); font-size: 14px; font-style: italic; }
  .event-box {
    position: absolute; left: 85px; top: 838px; width: 540px; height: 140px;
    border: 3px solid var(--navy); padding: 10px 18px;
  }
  .event-dates {
    display: inline-block; background: var(--navy); color: var(--orange);
    font-family: "Oswald", sans-serif; font-weight: 700; font-size: 34px; line-height: 1; padding: 4px 12px;
  }
  .venue { display: flex; gap: 12px; margin-top: 10px; }
  .venue svg { flex: none; margin-top: 4px; }
  .venue-lines { font-size: 16px; font-weight: 700; line-height: 1.3; color: var(--navy); }
  .venue-lines .venue-note { font-size: 13px; font-weight: 600; }
  .entry-fee { position: absolute; left: 660px; top: 840px; width: 150px; text-align: center; color: var(--navy); }
  .entry-price { font-family: "Oswald", sans-serif; font-weight: 700; font-size: 54px; line-height: 1; }
  .entry-label { font-weight: 800; font-size: 17px; }
  .entry-guarantee { font-weight: 600; font-size: 14px; line-height: 1.25; margin-top: 4px; }
  .weekday-note {
    position: absolute; left: 0; right: 0; top: 996px; text-align: center;
    font-size: 15px; font-style: italic; font-weight: 500; color: var(--navy);
  }
  .director { position: absolute; left: 88px; top: 1048px; color: var(--navy); }
  .block-heading { font-weight: 800; font-size: 15px; margin-bottom: 6px; }
  .contact-line { display: flex; align-items: center; gap: 10px; font-size: 14px; font-weight: 600; line-height: 1.5; }
  .sponsors { position: absolute; left: 456px; top: 1048px; width: 370px; color: var(--navy); }
  .sponsor-row { display: flex; gap: 10px; align-items: center; }
  .sponsor-stack { display: flex; flex-direction: column; gap: 6px; }
  .sponsor-name {
    background: var(--ink); color: var(--white); font-weight: 700; font-size: 12px;
    width: 120px; height: 32px; display: flex; align-items: center; justify-content: center;
  }
  .sponsor-badge { width: 56px; height: 56px; background: var(--navy); border-radius: 50%; }
  .sponsor-badge.square { border-radius: 4px; background: var(--ink); }
</style>
</head>
<body>
<main class="poster">
  <div class="brand-mark">BRAMWICK</div>

  <h1 class="title-club">WRENFOLD CLUB</h1>
  <div class="title-band">SYDNEY CBD SQUASH OPEN</div>
  <div class="title-year">2021</div>

  <div class="action-photo" role="img" aria-label="Squash player swinging a racquet in a dim court"></div>

  <div class="prize">$14,000 Grand Prize</div>
  <p class="entries-close">ENTRIES CLOSE ON<br>7th AUGUST 2021</p>

  <h2 class="grades-heading">GRADES AVAILABLE</h2>
  <ul class="grades-list">
    <li>Mens and Ladies</li>
    <li>Raquetball Open</li>
    <li>Squash Open</li>
    <li>Junior Events</li>
  </ul>
  <p class="grades-note">*All grades/abilities Catered for*</p>

  <section class="event-box">
    <div class="event-dates">AUGUST 13th-15th</div>
    <div class="venue">
      <svg width="22" height="30" viewBox="0 0 22 30" aria-hidden="true">
        <path d="M11 0C5 0 0 5 0 11c0 8 11 19 11 19s11-11 11-19C22 5 17 0 11 0z" fill="#1c2b4b"/>
        <circle cx="11" cy="11" r="4.5" fill="#f6a925"/>
      </svg>
      <div class="venue-lines">
        CBD COURTS (Wrenfold &amp; Ashgrove Clubs)<br>
        Harbourside University Sports &amp; Fitness<br>
        <span class="venue-note">(All finals will be held at the Wrenfold Club)</span>
      </div>
    </div>
  </section>

  <div class="entry-fee">
    <div class="entry-price">$60</div>
    <div class="entry-label">ENTRY FEE</div>
    <div class="entry-guarantee">Players guaranteed<br>3 Matches</div>
  </div>

  <p class="weekday-note">*Weekday Matches are also organised for CBD workers preferring to play during the day*</p>

  <section class="director">
    <div class="block-heading">TOURNAMENT DIRECTOR:</div>
    <div class="contact-line">Dylan Harwood</div>
    <div class="contact-line">
      <svg width="14" height="14" viewBox="0 0 24 24" aria-hidden="true"><path d="M6.6 10.8a15 15 0 0 0 6.6 6.6l2.2-2.2a1 1 0 0 1 1-.25 11.4 11.4 0 0 0 3.6.57 1 1 0 0 1 1 1V20a1 1 0 0 1-1 1A17 17 0 0 1 3 4a1 1 0 0 1 1-1h3.5a1 1 0 0 1 1 1c0 1.25.2 2.45.57 3.57a1 1 0 0 1-.25 1z" fill="#1c2b4b"/></svg>
      0412555918
    </div>
    <div class="contact-line">
      <svg width="14" height="14" viewBox="0 0 24 24" aria-hidden="true"><rect x="2" y="5" width="20" height="14" rx="2" fill="#1c2b4b"/><path d="M3 6l9 7 9-7" stroke="#f6a925" stroke-width="2" fill="none"/></svg>
      Dylan.Harwood@mailbox.net
    </div>
  </section>

  <section class="sponsors">
    <div class="block-heading">OUR SPONSORS:</div>
    <div class="sponsor-row">
      <div class="sponsor-stack">
        <div class="sponsor-name">WRENFOLD CLUB</div>
        <div class="sponsor-name">ASHGROVE</div>
      </div>
      <div class="sponsor-badge"></div>
      <div class="sponsor-badge square"></div>
      <div class="sponsor-badge"></div>
    </div>
  </section>
</main>
</body>
</html>
```